13 Tavo - new website design project

Our company Tavo Electrical is developing a new lead generation website focused on Electrical, LED Lighting and Solar Power. We need a high converting website.

Example of our current website is www.tavoelectrical.com.au You can take content from this website for this new design. Our colours are red, black and white. For our new website we would like to promote Tavo, Bright Days Ahead. Please listen to the jingle.

The below link is the company jingle that we have developed.
http://www.tunecraftaudio.com.au/tav-tc-v1/

The key for this brief is to generate leads for Electrical, LED Lighting (for commercial) and Solar Power & Storage.

Target Market(s)

Business owners in Melbourne Victoria

Number of Pages Required

4 page

Colors
ec1f27
ffffff

Requirements
Must have
• This page must be clean, be in line with company branding and a high converting lead website.

```html
<!DOCTYPE html>
<html lang="en">
<head>
<meta charset="utf-8">
<title>Tavo Electrical – Electrical, LED Lighting, Solar Power</title>
<link href="https://fonts.googleapis.com/css2?family=Roboto:ital,wght@0,300;0,400;0,500;0,700;1,400&display=swap" rel="stylesheet">
<style>
:root{
  --red:#d8232a;
  --red-bright:#ec1f27;
  --ink:#1f1f1f;
  --charcoal:#23262d;
  --black:#0b0b0b;
  --grey-band:#f3f1f2;
  --grey-section:#efeff0;
  --grey-mid:#e4e4e6;
  --text:#555;
  --white:#fff;
}
*{box-sizing:border-box;margin:0;padding:0}
html,body{width:1200px;height:2307px;overflow:hidden}
body{position:relative;font-family:'Roboto',Arial,sans-serif;color:var(--ink);background:var(--white)}
.abs{position:absolute}

/* header */
.site-header{position:absolute;left:0;top:0;width:1200px;height:57px;background:var(--white)}
.brand-tab{position:absolute;left:0;top:0;width:380px;height:57px;background:#e3e1e2;clip-path:polygon(0 0,100% 0,88% 100%,0 100%)}
.brand{position:absolute;left:255px;top:8px;display:flex;align-items:center;gap:8px}
.brand-mark{width:14px;height:14px;background:var(--red)}
.brand-name{font-weight:700;font-size:26px;color:var(--ink);line-height:1}
.brand-tag{position:absolute;left:262px;top:38px;font-size:9px;color:var(--ink)}
.top-phone{position:absolute;right:250px;top:4px;display:flex;align-items:center;gap:4px;font-size:16px;font-weight:500}
.top-phone .tag{background:var(--red);color:#fff;font-size:11px;font-weight:700;padding:1px 5px}
.nav-strip{position:absolute;left:470px;top:32px;width:730px;height:25px;background:#ececec}
.main-nav{position:absolute;left:483px;top:38px;display:flex;gap:15px;font-size:10.5px;font-weight:500;text-transform:uppercase}

/* hero */
.hero{position:absolute;left:0;top:57px;width:1200px;height:369px;background:linear-gradient(90deg,#d9dadc 0%,#f1f1f1 40%,#fafafa 70%,#eeeeee 100%);border-bottom:2px solid var(--red)}
.hero-person{position:absolute;left:217px;top:0;width:193px;height:369px;background:linear-gradient(180deg,#c88d6c 0%,#2a3140 30%,#222a38 100%);border-radius:80px 80px 0 0}
.hero-caption{position:absolute;left:395px;top:113px;width:255px;height:70px;background:#2b2b2d;padding:10px 14px;color:#fff}
.hero-caption .kicker{color:var(--red-bright);font-size:9.5px;text-transform:uppercase;margin-bottom:6px}
.hero-caption p{font-size:10.5px;line-height:1.3;font-weight:300}
.hero-tiles{position:absolute;left:632px;top:13px}

/* welcome */
.welcome{position:absolute;left:0;top:428px;width:1200px;height:160px;background:var(--grey-band);text-align:center}
.welcome h1{font-size:24px;font-weight:400;margin-top:22px;letter-spacing:.5px}
.divider{position:relative;width:445px;height:10px;margin:8px auto 0}
.divider::before{content:"";position:absolute;left:0;right:0;top:5px;border-top:1px solid #444}
.divider::after{content:"";position:absolute;left:218px;top:1px;width:7px;height:7px;border:1.5px solid var(--red);background:var(--grey-band);transform:rotate(45deg)}
.welcome p{width:690px;margin:10px auto 0;font-size:10.5px;line-height:1.6;color:#777}
.welcome-pointer{position:absolute;left:592px;top:588px;width:0;height:0;border-left:8px solid transparent;border-right:8px solid transparent;border-top:8px solid var(--red)}

/* service cards */
.service-card{position:absolute;top:622px;width:225px;height:335px;background:var(--grey-band);text-align:center}
.service-card .photo{height:145px;border-bottom:3px solid var(--red)}
.service-card .badge{position:absolute;left:100px;top:131px;width:26px;height:26px;background:var(--red);transform:rotate(45deg)}
.service-card h2{font-size:15px;font-weight:400;margin-top:30px}
.service-card p{font-size:10px;line-height:1.55;color:#555;margin:10px 16px 0}
.btn-dark{display:inline-block;margin-top:13px;width:147px;height:32px;line-height:32px;background:var(--charcoal);color:#fff;font-size:13.5px}

/* why choose us */
.why{position:absolute;left:0;top:994px;width:1200px;height:539px;background:var(--grey-section)}
.why h2{position:absolute;top:36px;width:100%;text-align:center;font-size:24px;font-weight:400}
.why-rail{position:absolute;left:301px;top:150px;width:3px;height:320px;background:var(--red)}
.why-item{position:absolute;left:272px;width:700px}
.why-num{position:absolute;left:0;top:0;width:62px;height:62px;border-radius:50%;background:var(--charcoal);border:4px solid var(--red);box-shadow:0 0 0 3px #fff inset;color:#fff;font-size:21px;font-weight:500;text-align:center;line-height:54px}
.why-item h3{position:absolute;left:79px;top:4px;color:var(--red);font-size:15px;font-weight:400;white-space:nowrap}
.why-item p{position:absolute;left:79px;top:28px;width:580px;font-size:10px;line-height:1.7;color:#555}

/* clients */
.clients-title{position:absolute;top:1574px;width:100%;text-align:center;font-size:24px;font-weight:400}
.clients-band{position:absolute;left:0;top:1628px}
.client-logo{position:absolute;width:144px;height:85px;background:#fff;border:1px solid #d6d6d6;padding:5px}
.client-logo span{display:flex;align-items:center;justify-content:center;width:100%;height:100%;font-size:13px;font-weight:700;text-align:center;line-height:1.2;padding:4px}
.review{position:absolute;left:633px;top:1705px;width:300px;color:#fff}
.review-avatar{position:absolute;left:0;top:0;width:58px;height:58px;border-radius:50%;background:#bbb;border:5px solid #fff}
.review-name{position:absolute;left:65px;top:18px;font-size:11px;line-height:1.2}
.review-name small{display:block;font-size:10px;color:#ccc}
.review blockquote{position:absolute;left:12px;top:72px;width:300px;font-style:italic;font-size:11.5px;line-height:1.55}
.dots{position:absolute;left:649px;top:1868px;display:flex;gap:5px}
.dots i{width:6px;height:6px;border-radius:50%;background:#fff}
.dots i.on{background:var(--red)}

/* footer */
.site-footer{position:absolute;left:0;top:1998px;width:1200px;height:281px;background:var(--black);color:#fff}
.footer-rule{position:absolute;left:600px;top:33px;width:1px;height:215px;background:#333}
.footer-brand{position:absolute;left:373px;top:60px;display:flex;align-items:center;gap:7px;font-size:24px;font-weight:700}
.footer-brand .brand-mark{width:12px;height:12px}
.footer-about{position:absolute;left:373px;top:108px;width:232px;font-size:9px;line-height:1.55;color:#ddd}
.btn-red{position:absolute;left:373px;top:200px;width:90px;height:19px;line-height:19px;text-align:center;background:var(--red);color:#fff;font-size:9px;border-radius:2px}
.footer-phone{position:absolute;left:628px;top:49px}
.footer-phone .num{display:flex;align-items:center;gap:5px;margin-top:4px;font-size:24px;font-weight:500}
.footer-phone .tag{background:var(--red);font-size:14px;font-weight:700;padding:2px 6px}
.social{position:absolute;left:630px;top:124px;display:flex;gap:8px}
.social i{width:28px;height:28px;border-radius:50%;background:#555;border:2px solid #fff}
.quick{position:absolute;left:639px;top:186px}
.quick h4{color:var(--red);font-size:11px;font-weight:400}
.quick ul{list-style:none;display:flex;gap:8px;font-size:9px;margin-top:6px}
.bottom-bar{position:absolute;left:0;top:2279px;width:1200px;height:28px;background:#222;color:#ccc;font-size:8.5px;text-align:center;line-height:28px}
</style>
</head>
<body>

<header class="site-header">
  <div class="brand-tab"></div>
  <div class="brand"><span class="brand-mark"></span><span class="brand-name">TAVO</span></div>
  <div class="brand-tag">Bright Days Ahead</div>
  <div class="top-phone">
    <svg width="14" height="12" viewBox="0 0 14 12"><path d="M1 4c0-2 3-3 6-3s6 1 6 3l-2 1-1-2H4L3 5z M3 6h8l1 5H2z" fill="#d8232a"/></svg>
    137264 <span class="tag">TAVO</span>
  </div>
  <div class="nav-strip"></div>
  <nav class="main-nav">
    <span>Home</span><span>Tavo Story</span><span>Our Work</span><span>Contact Us</span><span>Electrical</span><span>LED Lighting</span><span>Solar Power</span>
  </nav>
</header>

<section class="hero">
  <div class="hero-person" role="img" aria-label="Smiling electrician in work uniform with arms crossed"></div>
  <div class="hero-caption">
    <div class="kicker">Electrical LED Lighting Solar Power</div>
    <p>Australia's largest fully integrated Electrical &amp; energy Solutions Provider</p>
  </div>
  <svg class="hero-tiles" width="424" height="340" viewBox="0 0 424 340">
    <polygon role="img" aria-label="Electrician testing a switchboard" points="125,0 215,0 240,90 185,170 95,130 85,40" fill="#8a3a36"/>
    <polygon role="img" aria-label="Technician installing solar panels" points="0,110 75,95 140,170 135,260 50,263 10,200" fill="#3d6d9e"/>
    <polygon role="img" aria-label="Glowing LED light bulb" points="200,175 280,130 420,190 405,263 230,263" fill="#2d7dc7"/>
  </svg>
</section>

<section class="welcome">
  <h1>WELCOME  TO TAVO</h1>
  <div class="divider"></div>
  <p>Lorem Ipsum is simply dummy text of the printing and typesetting industry. Lorem Ipsum has been the industry's standard dummy text ever since the 1500s, when an unknown printer took a galley of type and scrambled it to make a type specimen book. It has survived not only five centuries, but also the leap into electronic typesetting.</p>
</section>
<div class="welcome-pointer"></div>

<article class="service-card" style="left:249px">
  <div class="photo" role="img" aria-label="Workers installing rooftop solar panels" style="background:linear-gradient(135deg,#e9b07a,#5f7ea8)"></div>
  <span class="badge"></span>
  <h2>Solar Power</h2>
  <p>Lorem Ipsum is simply dummy text of the printing and typesetting industry. Lorem Ipsum has been the industry's standard dummy text ever since the 1500s, when an unknown printer took a galley of type and scrambled it</p>
  <span class="btn-dark">Read More</span>
</article>
<article class="service-card" style="left:488px">
  <div class="photo" role="img" aria-label="Row of glowing LED bulbs" style="background:radial-gradient(circle at 55% 60%,#dbeeff,#1f6fc0 40%,#0d2f6b)"></div>
  <span class="badge"></span>
  <h2>Led Lighting</h2>
  <p>Lorem Ipsum is simply dummy text of the printing and typesetting industry. Lorem Ipsum has been the industry's standard dummy text ever since the 1500s, when an unknown printer took a galley of type and scrambled it</p>
  <span class="btn-dark">Read More</span>
</article>
<article class="service-card" style="left:726px">
  <div class="photo" role="img" aria-label="Circuit breakers being tested with a screwdriver" style="background:linear-gradient(135deg,#7a2a25,#c8c0b5 60%,#5a1b18)"></div>
  <span class="badge"></span>
  <h2>Electrical</h2>
  <p>Lorem Ipsum is simply dummy text of the printing and typesetting industry. Lorem Ipsum has been the industry's standard dummy text ever since the 1500s, when an unknown printer took a galley of type and scrambled it</p>
  <span class="btn-dark">Read More</span>
</article>

<section class="why">
  <h2>WHY CHOOSE US?</h2>
  <div class="why-rail"></div>
  <div class="why-item" style="top:92px"><div class="why-num">1</div><h3>Professional service</h3><p>When you hire a Tavo Electrical Electrician you will get a professional and well-presented Electrician that comes skilled and ready to do the job</p></div>
  <div class="why-item" style="top:180px"><div class="why-num">2</div><h3>5 year workmanship guarantee</h3><p>You can buy with confidence as all of our work has a 5 year workmanship guarantee. For your peace of mind, we unconditionally back our electrical work. We will come back to fix any problems at our own expense.</p></div>
  <div class="why-item" style="top:268px"><div class="why-num">3</div><h3>Value for Money</h3><p>We provide extremely competitive pricing, which means you get value for money on quality that is comparable to the best in the industry.</p></div>
  <div class="why-item" style="top:355px"><div class="why-num">4</div><h3>Environmentally friendly</h3><p>We a committed to reducing carbon emissions by installing Solar Power and upgrading sites to LED Lighting. In addition to reducing the carbon emissions we recycle Fluorescent Tubes, Highbay Globes, Metal and Cardboard.</p></div>
  <div class="why-item" style="top:441px"><div class="why-num">5</div><h3>Fully insured</h3><p>Tavo Electrical is fully insured and equipped to handle break downs and service call outs.</p></div>
</section>

<h2 class="clients-title">OUR SATISFIED CLIENTS INCLUDE...</h2>
<svg class="clients-band" width="1200" height="318" viewBox="0 0 1200 318">
  <polygon points="0,33 594,0 594,318 0,285" fill="#e4e4e6"/>
  <polygon points="594,0 1200,38 1200,283 594,318" fill="#23262d"/>
</svg>
<div class="client-logo" style="left:248px;top:1692px"><span style="color:#d8232a">Goldarch Diner</span></div>
<div class="client-logo" style="left:406px;top:1692px"><span style="color:#d8232a">Heron Plumbing Supplies</span></div>
<div class="client-logo" style="left:248px;top:1793px"><span style="color:#1f1f1f">Outback Surplus</span></div>
<div class="client-logo" style="left:406px;top:1793px"><span style="color:#d8232a">Velvetline</span></div>

<div class="review">
  <div class="review-avatar"></div>
  <div class="review-name">Marlow<small>Brookvale North VIC</small></div>
  <blockquote>Excellent work and very professional. Declan takes time to explain everything and demonstrate workings. Very clear precise and accurate."</blockquote>
</div>
<div class="dots"><i></i><i class="on"></i><i></i></div>

<footer class="site-footer">
  <div class="footer-brand"><span class="brand-mark"></span>TAVO</div>
  <p class="footer-about">Tavo Electrical was formed to be an expert Electricity Contracting Company providing services to all Residential and Commercial Customers. With over 10 years of experience, Tavo Electrical has developed a highly-experienced team of professionals that ensure all our customer expectations are met.</p>
  <span class="btn-red">Read More</span>
  <div class="footer-rule"></div>
  <div class="footer-phone">
    <svg width="18" height="15" viewBox="0 0 14 12"><path d="M1 4c0-2 3-3 6-3s6 1 6 3l-2 1-1-2H4L3 5z M3 6h8l1 5H2z" fill="#d8232a"/></svg>
    <div class="num">137264 <span class="tag">TAVO</span></div>
  </div>
  <div class="social"><i></i><i></i><i></i><i></i></div>
  <div class="quick">
    <h4>Quick Link</h4>
    <ul><li>Led Lighting</li><li>Solar Power</li><li>Electrical</li><li>Career</li></ul>
  </div>
</footer>
<div class="bottom-bar">A © 2016 All rights reserved | Privacy Policy. Design &amp; Development by brightpixel.com.au</div>

</body>
</html>
```